Business Card cabinets and cabinets components making company.

the card should be formal and interesting at the same time. The main colors will be black and white.

Font styles to use
Sans Serif

Colors

Designer to choose only greyscale colors for use in the design.

Requirements
Must have
• At least must have the followings:
office phone
cell phone
address
position
name
email
web

```html
<!DOCTYPE html>
<html lang="en">
<head>
<meta charset="utf-8">
<title>Daniel Marsh – Business Card</title>
<link rel="stylesheet" href="https://fonts.googleapis.com/css2?family=Outfit:wght@300;400;500&display=swap">
<style>
  :root {
    --paper: #ffffff;
    --ink: #111111;
    --ink-name: #333333;
    --ink-soft: #4a4a4a;
    --ink-muted: #7a7a7a;
    --rule: #c8c8c8;
    --trim: #1a1a1a;
  }
  * { margin: 0; padding: 0; box-sizing: border-box; }
  html, body { width: 1200px; height: 764px; overflow: hidden; background: var(--paper); }
  .card {
    position: relative;
    width: 1200px;
    height: 764px;
    background: var(--paper);
    font-family: "Outfit", sans-serif;
    color: var(--ink);
  }
  .trim-marks { position: absolute; inset: 0; }
  .holder {
    position: absolute;
    left: 179px;
    top: 186px;
  }
  .holder-name {
    font-size: 32px;
    font-weight: 400;
    letter-spacing: 0.3px;
    color: var(--ink-name);
    line-height: 40px;
  }
  .holder-role {
    display: flex;
    align-items: center;
    gap: 12px;
    margin-top: 4px;
    height: 22px;
    font-size: 15px;
    font-weight: 500;
    letter-spacing: 3px;
    text-transform: uppercase;
    color: var(--ink-muted);
  }
  .holder-role::before {
    content: "";
    width: 34px;
    height: 2px;
    background: var(--ink);
  }
  .address {
    margin-top: 14px;
    font-style: normal;
    font-size: 24px;
    font-weight: 300;
    line-height: 32px;
    color: var(--ink-soft);
  }
  .contacts {
    list-style: none;
    margin-top: 12px;
  }
  .contact {
    display: flex;
    align-items: center;
    height: 33px;
    font-size: 24px;
    font-weight: 300;
    color: var(--ink);
  }
  .contact-icon {
    width: 20px;
    height: 20px;
    margin-right: 12px;
    flex: none;
  }
  .social {
    display: flex;
    gap: 18px;
    margin-top: 30px;
    list-style: none;
  }
  .social-item {
    display: flex;
    align-items: center;
    gap: 7px;
    font-size: 18px;
    font-weight: 400;
    color: var(--ink);
  }
  .social-dot {
    width: 14px;
    height: 14px;
    border-radius: 50%;
    background: var(--ink);
  }
  .edge-rule {
    position: absolute;
    left: 144px;
    top: 194px;
    width: 2px;
    height: 60px;
    background: var(--ink);
  }
</style>
</head>
<body>
<main class="card">
  <svg class="trim-marks" width="1200" height="764" viewBox="0 0 1200 764" aria-hidden="true">
    <g stroke="var(--trim)" stroke-width="1.5">
      <line x1="88" y1="0" x2="88" y2="45"/>
      <line x1="1092" y1="0" x2="1092" y2="45"/>
      <line x1="88" y1="719" x2="88" y2="764"/>
      <line x1="1092" y1="719" x2="1092" y2="764"/>
      <line x1="0" y1="93" x2="46" y2="93"/>
      <line x1="1154" y1="93" x2="1200" y2="93"/>
      <line x1="0" y1="667" x2="46" y2="667"/>
      <line x1="1154" y1="667" x2="1200" y2="667"/>
    </g>
  </svg>

  <span class="edge-rule" aria-hidden="true"></span>

  <section class="holder">
    <h1 class="holder-name">DANIEL MARSH</h1>
    <p class="holder-role">Head of Cabinet Design</p>
    <address class="address">
      2290 Alder Grove Road<br>
      Suite 310, Houston<br>
      TX 77041
    </address>

    <ul class="contacts">
      <li class="contact">
        <svg class="contact-icon" viewBox="0 0 24 24" aria-label="Office phone"><path fill="currentColor" d="M6.6 10.8c1.4 2.8 3.8 5.1 6.6 6.6l2.2-2.2c.3-.3.7-.4 1-.2 1.1.4 2.3.6 3.6.6.6 0 1 .4 1 1V20c0 .6-.4 1-1 1C10.6 21 3 13.4 3 4c0-.6.4-1 1-1h3.5c.6 0 1 .4 1 1 0 1.3.2 2.5.6 3.6.1.3 0 .7-.2 1l-2.3 2.2z"/></svg>
        +1-713-555-0148
      </li>
      <li class="contact">
        <svg class="contact-icon" viewBox="0 0 24 24" aria-label="Mobile phone"><rect x="6.5" y="2" width="11" height="20" rx="2" fill="none" stroke="currentColor" stroke-width="1.8"/><line x1="10.5" y1="18.5" x2="13.5" y2="18.5" stroke="currentColor" stroke-width="1.6"/></svg>
        +1-713-555-0193
      </li>
      <li class="contact">
        <svg class="contact-icon" viewBox="0 0 24 24" aria-label="Email"><path fill="currentColor" d="M3 5h18v14H3z"/><path fill="none" stroke="#fff" stroke-width="1.6" d="M4 6.5l8 6 8-6"/></svg>
        hello@marshcabinetry.com
      </li>
      <li class="contact">
        <svg class="contact-icon" viewBox="0 0 24 24" aria-label="Website"><g fill="none" stroke="currentColor" stroke-width="1.5"><circle cx="12" cy="12" r="9"/><ellipse cx="12" cy="12" rx="4" ry="9"/><line x1="3" y1="12" x2="21" y2="12"/><line x1="4.5" y1="7.5" x2="19.5" y2="7.5"/><line x1="4.5" y1="16.5" x2="19.5" y2="16.5"/><line x1="12" y1="3" x2="12" y2="21"/></g></svg>
        www.marshcabinetry.com
      </li>
    </ul>

    <ul class="social">
      <li class="social-item"><span class="social-dot"></span>Friendwall</li>
      <li class="social-item"><span class="social-dot"></span>Workroll</li>
      <li class="social-item"><span class="social-dot"></span>Viewcast</li>
      <li class="social-item"><span class="social-dot"></span>Snapframe</li>
    </ul>
  </section>
</main>
</body>
</html>
```